Oil and Gas Exploration and Production company needs a business card design

We need a business card design using our logo and colors in the logo. We want a mainstream design.

```html
<!DOCTYPE html>
<html lang="en">
<head>
<meta charset="utf-8">
<title>Kelvo business cards</title>
<link rel="stylesheet" href="https://fonts.googleapis.com/css2?family=Merriweather:wght@400;700;900&display=swap">
<style>
  :root {
    --backdrop: #bcbdbf;
    --ink: #1c1a1b;
    --card-dark: #1b191a;
    --card-dark-deep: #0f0e0f;
    --paper: #ffffff;
    --gold: #c8952f;
    --text: #2a2728;
  }
  * { box-sizing: border-box; margin: 0; padding: 0; }
  html, body { width: 1200px; height: 822px; overflow: hidden; }
  body {
    background: var(--backdrop);
    font-family: "Merriweather", Georgia, serif;
    color: var(--text);
    position: relative;
  }
  .card {
    position: absolute;
    width: 490px;
    height: 279px;
    box-shadow: 0 2px 10px rgba(0,0,0,0.28);
    overflow: hidden;
  }
  .card--pattern-back { left: 88px; top: 88px; background: var(--card-dark); }
  .card--front-classic { left: 622px; top: 88px; background: var(--paper); }
  .card--mark-back { left: 88px; top: 455px; background: var(--card-dark); }
  .card--front-accent { left: 622px; top: 455px; background: var(--paper); }

  /* pattern back */
  .pattern-fill {
    position: absolute; inset: 0;
    background: linear-gradient(160deg, #232122 0%, #141314 100%);
  }
  .back-url {
    position: absolute; left: 0; right: 0; top: 241px;
    text-align: center;
    color: var(--gold);
    font-weight: 700;
    font-size: 16px;
    letter-spacing: 2px;
    line-height: 1.2;
  }

  /* wordmark */
  .wordmark {
    position: absolute;
    display: flex; align-items: center; gap: 8px;
    font-weight: 900;
    color: var(--ink);
    line-height: 1;
    white-space: nowrap;
  }
  .wordmark__dot {
    border-radius: 50%;
    background: var(--ink);
    flex: none;
  }
  .wordmark--classic { left: 18px; top: 34px; font-size: 62px; }
  .wordmark--classic .wordmark__dot { width: 36px; height: 36px; }
  .wordmark--accent { right: 19px; top: 34px; font-size: 54px; }
  .wordmark--accent .wordmark__dot { width: 32px; height: 32px; }
  .wordmark--embossed {
    left: 0; right: 0; top: 95px; justify-content: center;
    font-size: 92px; color: var(--card-dark-deep); gap: 12px;
  }
  .wordmark--embossed .wordmark__dot { width: 54px; height: 54px; background: var(--card-dark-deep); }

  /* classic front */
  .side-rule {
    position: absolute; left: 459px; top: 0; width: 6px; height: 100%;
    background: var(--ink);
  }
  .holder { position: absolute; line-height: 1.2; }
  .holder__name { font-weight: 900; font-size: 16.5px; letter-spacing: 0.2px; }
  .holder__title { font-size: 12px; margin-top: 2px; }
  .holder--right { right: 44px; top: 152px; text-align: right; }
  .holder--right .holder__name { color: var(--gold); }
  .holder--left { left: 28px; top: 121px; }
  .holder--left .holder__name { color: var(--ink); }

  .contact-stack {
    position: absolute; right: 21px; top: 202px;
    list-style: none;
    display: flex; flex-direction: column; gap: 2px;
  }
  .contact-stack li {
    display: flex; align-items: center; justify-content: flex-end; gap: 7px;
    font-size: 13px; height: 18.5px; line-height: 1;
  }
  .icon-box {
    width: 18px; height: 18px;
    border: 2px solid var(--ink);
    background: var(--paper);
    display: flex; align-items: center; justify-content: center;
  }
  .icon { width: 10px; height: 10px; fill: var(--ink); }

  /* accent front */
  .edge-band {
    position: absolute; left: 0; top: 0; width: 9px; height: 100%;
    background: var(--gold);
  }
  .contact-list {
    position: absolute; left: 285px; top: 122px; width: 186px;
    list-style: none;
  }
  .contact-list li {
    display: flex; align-items: flex-start; gap: 6px;
    font-size: 13px;
    border-bottom: 2px solid var(--ink);
    padding: 0 0 6px;
    margin-bottom: 8px;
    line-height: 1.35;
  }
  .contact-list .icon { margin-top: 4px; flex: none; }
</style>
</head>
<body>

<section class="card card--pattern-back" aria-label="Card back with pattern">
  <div class="pattern-fill" role="img" aria-label="Repeating dark droplet pattern"></div>
  <p class="back-url">www.KELVO.com</p>
</section>

<section class="card card--front-classic" aria-label="Card front, classic layout">
  <div class="wordmark wordmark--classic"><span class="wordmark__dot"></span>Kelvo</div>
  <div class="side-rule"></div>
  <div class="holder holder--right">
    <p class="holder__name">YOUR NAME</p>
    <p class="holder__title">Title</p>
  </div>
  <ul class="contact-stack">
    <li>123.456.7890
      <span class="icon-box"><svg class="icon" viewBox="0 0 10 10"><path d="M2 0.5 L3.8 2.6 L2.9 3.6 Q4 5.8 6.4 7.1 L7.4 6.2 L9.5 8 L8.2 9.5 Q3.5 9 0.5 1.8 Z"/></svg></span></li>
    <li>name@Kelvo.com
      <span class="icon-box"><svg class="icon" viewBox="0 0 10 10"><path d="M0.5 2 H9.5 V8 H0.5 Z M0.5 2 L5 5.5 L9.5 2" stroke="#fff" stroke-width="0.8"/></svg></span></li>
    <li>456 Ridge Road Fairhaven, Texas 70001
      <span class="icon-box"><svg class="icon" viewBox="0 0 10 10"><path d="M5 0.3 A3.3 3.3 0 0 1 8.3 3.6 C8.3 6 5 9.7 5 9.7 C5 9.7 1.7 6 1.7 3.6 A3.3 3.3 0 0 1 5 0.3 Z M5 2.3 A1.3 1.3 0 1 0 5 4.9 A1.3 1.3 0 1 0 5 2.3 Z" fill-rule="evenodd"/></svg></span></li>
  </ul>
</section>

<section class="card card--mark-back" aria-label="Card back with name">
  <div class="wordmark wordmark--embossed"><span class="wordmark__dot"></span>Kelvo</div>
</section>

<section class="card card--front-accent" aria-label="Card front, accent layout">
  <div class="edge-band"></div>
  <div class="wordmark wordmark--accent"><span class="wordmark__dot"></span>Kelvo</div>
  <div class="holder holder--left">
    <p class="holder__name">YOUR NAME</p>
    <p class="holder__title">Title</p>
  </div>
  <ul class="contact-list">
    <li><svg class="icon" viewBox="0 0 10 10"><path d="M2 0.5 L3.8 2.6 L2.9 3.6 Q4 5.8 6.4 7.1 L7.4 6.2 L9.5 8 L8.2 9.5 Q3.5 9 0.5 1.8 Z"/></svg>123.456.7890</li>
    <li><svg class="icon" viewBox="0 0 10 10"><path d="M0.5 2 H9.5 V8 H0.5 Z M0.5 2 L5 5.5 L9.5 2" stroke="#fff" stroke-width="0.8"/></svg>name@Kelvo.com</li>
    <li><svg class="icon" viewBox="0 0 10 10"><circle cx="5" cy="5" r="4.3" fill="none" stroke="#1c1a1b" stroke-width="1"/><path d="M0.7 5 H9.3 M5 0.7 V9.3 M5 0.7 Q2.5 5 5 9.3 M5 0.7 Q7.5 5 5 9.3" fill="none" stroke="#1c1a1b" stroke-width="0.8"/></svg>www.Kelvo.com</li>
    <li><svg class="icon" viewBox="0 0 10 10"><path d="M5 0.3 A3.3 3.3 0 0 1 8.3 3.6 C8.3 6 5 9.7 5 9.7 C5 9.7 1.7 6 1.7 3.6 A3.3 3.3 0 0 1 5 0.3 Z M5 2.3 A1.3 1.3 0 1 0 5 4.9 A1.3 1.3 0 1 0 5 2.3 Z" fill-rule="evenodd"/></svg><span>456 Ridge Road<br>Fairhaven, Texas 70001</span></li>
  </ul>
</section>

</body>
</html>
```